Cedarline Joinery eye catching business card

I need an eye catching business card that reflects my traditional, fun, handmade woodcraft shop. I make high end custom furniture and fine woodworking products, a lot of which are rustic, natural looking. We are a small shop but we produce awesome, one of a kind wood products, and our business card should reflect that. Our target audience is young professionals to retired folks who want a quality, local, handmade product. I'd like the Shop Nearby logo somewhere on the card, BUT not overwhelming, the main focus is my Logo, no preference on color whichever looks the best. Visit my website to get a feel for my company. Cedarlinejoinery.com
Target Market(s)
young professionals to retired folks. Any one who wants to furnish their home with quality handcrafted products.
Industry/Entity Type
Business
Contact Information for Business Card
Marlo Finch (555)417-6382
marlo@cedarlinejoinery.com
www.cedarlinejoinery.com
Look and feel

```html
<!DOCTYPE html>
<html lang="en">
<head>
<meta charset="utf-8">
<title>Cedarline Joinery – Business Card</title>
<link href="https://fonts.googleapis.com/css2?family=Source+Sans+3:wght@400;600&display=swap" rel="stylesheet">
<style>
  :root {
    --backdrop: #1b1b1b;
    --card-white: #ffffff;
    --card-black: #000000;
    --ink: #111111;
    --ink-soft: #4a4a4a;
    --paper: #ffffff;
  }
  * { margin: 0; padding: 0; box-sizing: border-box; }
  html, body {
    width: 1200px;
    height: 900px;
    overflow: hidden;
    background: var(--backdrop);
    font-family: "Source Sans 3", "Myriad Pro", Arial, sans-serif;
  }
  .card {
    position: absolute;
    top: 309px;
    width: 432px;
    height: 250px;
    border-radius: 14px;
    overflow: hidden;
  }
  .card--front { left: 153px; background: var(--card-white); }
  .card--back { left: 632px; background: var(--card-black); }

  /* front: brand band */
  .brand-band {
    position: absolute;
    left: 17px;
    top: 0;
    width: 115px;
    height: 100%;
    background: var(--card-black);
  }
  .brand-band__name {
    position: absolute;
    left: 50%;
    top: 50%;
    width: 250px;
    transform: translate(-50%, -50%) rotate(-90deg);
    text-align: center;
    color: var(--paper);
    font-weight: 600;
    text-transform: uppercase;
    line-height: 1;
  }
  .brand-band__line { display: block; }
  .brand-band__line--main { font-size: 36px; letter-spacing: 3px; }
  .brand-band__line--sub { font-size: 36px; letter-spacing: 3px; margin-top: 6px; }

  /* front: contact details */
  .contact {
    position: absolute;
    left: 205px;
    top: 48px;
    color: var(--ink-soft);
    font-size: 12.5px;
    line-height: 15px;
  }
  .contact__name {
    color: var(--ink);
    font-weight: 600;
    font-size: 17.5px;
    line-height: 20px;
  }
  .contact__role { margin-bottom: 11px; }
  .contact__address { margin-bottom: 11px; }
  .contact__list { list-style: none; }
  .contact__item {
    display: flex;
    align-items: center;
    height: 16.3px;
  }
  .contact__icon {
    width: 9px;
    height: 9px;
    margin-right: 8px;
    flex: none;
    fill: var(--ink);
  }

  /* back: brand */
  .back-brand {
    position: absolute;
    left: 0;
    right: 0;
    top: 88px;
    text-align: center;
    color: var(--paper);
  }
  .back-brand__name {
    font-weight: 600;
    font-size: 31px;
    letter-spacing: 2px;
    text-transform: uppercase;
    line-height: 1;
  }
  .back-brand__tagline {
    margin-top: 38px;
    font-size: 6px;
    font-weight: 600;
    letter-spacing: 1px;
    text-transform: uppercase;
  }
</style>
</head>
<body>

<section class="card card--front" aria-label="Business card front">
  <div class="brand-band">
    <div class="brand-band__name">
      <span class="brand-band__line brand-band__line--main">Cedarline</span>
      <span class="brand-band__line brand-band__line--sub">Joinery</span>
    </div>
  </div>

  <div class="contact">
    <p class="contact__name">Jonathan Smith</p>
    <p class="contact__role">Managing Director</p>
    <p class="contact__address">1234, Address Goes Here<br>Country Name, 123456</p>
    <ul class="contact__list">
      <li class="contact__item">
        <svg class="contact__icon" viewBox="0 0 10 10" aria-hidden="true"><path d="M2.5 0h5v10h-5zM3.5 1v7h3V1z"/></svg>
        123-456-7890
      </li>
      <li class="contact__item">
        <svg class="contact__icon" viewBox="0 0 10 10" aria-hidden="true"><path d="M0 3c2-2 8-2 10 0v1.5H7.5V3h-5v1.5H0zM2 5h6l1 4H1z"/></svg>
        123-456-7890
      </li>
      <li class="contact__item">
        <svg class="contact__icon" viewBox="0 0 10 10" aria-hidden="true"><path d="M2.5 0h4l1 1v3h-5zM1 4.5h8V10H1zM3 6v1h4V6z"/></svg>
        123-456-7890
      </li>
      <li class="contact__item">
        <svg class="contact__icon" viewBox="0 0 10 10" aria-hidden="true"><path d="M0 2h10v.8L5 6 0 2.8zM0 4l5 3 5-3v5H0z"/></svg>
        info@youremail.com
      </li>
      <li class="contact__item">
        <svg class="contact__icon" viewBox="0 0 10 10" aria-hidden="true"><path d="M6 0.5l3.5 3.5-2.5 2.5-1-1 1.5-1.5L6 2.5 4.5 4l-1-1zM4 9.5L.5 6 3 3.5l1 1L2.5 6 4 7.5 5.5 6l1 1z"/></svg>
        www.yourweb.com
      </li>
    </ul>
  </div>
</section>

<section class="card card--back" aria-label="Business card back">
  <div class="back-brand">
    <p class="back-brand__name">Cedarline Joinery</p>
    <p class="back-brand__tagline">Handmade in Cedar Harbor</p>
  </div>
</section>

</body>
</html>
```